Website redesign for a Cloud Advisory business

We are looking to revisit our existing brand and website, with a view to updating both. Looking for concepts and designs for how the website might look, flow and feel. Current website is: www.brellomint.com.au

Scope and Deliverables: Concept design for the home page and one internal page.

We do not expect you to design all the pages and all the elements of the website at this stage.

This job is not for the full website design, but just for concepts that we can start with when we go into the full website design.

We would love to see a design feature based on our name, logo, or industry, which can run through banners and other collateral (twitter banner, ads on Google, corporate documents etc).

We want the brand to properly depict what we bring/deliver to businesses when consulting to them and this should extend to the colour scheme, logo, font (perhaps updated) and copy (which will be supplied).

Our brand should suitably communicate our ability, knowledge and extensive experience within the Cloud space.

It should express and evoke credibility, knowledge and understanding of the Cloud space, independence, gravitas, reliability, efficiency, trust, expertise, approachability, service delivery but be uncomplicated, practical and use plain speaking language.

Colours that reinforce this might include: Blues, blacks, silver, white, grey and our existing orange.

Website designs that we like or have referenced include:

Varnolift: http://varnolift.com.au/ - This has good information but looks a little amateur in it’s cartoon like design and colour scheme. Also, this seems to be aimed at clients more interested in price than design and what we are going for is a little more high end.

Pendramoor: https://www.pendramoor.com.au/ - This site has merit in its’ setup but little call to action on the home page, especially before the scroll line. I like the set up of the Case Studies page however I’d look to make it more prominent by having it set up 3 across rather than the 4 they have. Something such as this: https://www.qandelby.com/case-studies

Tolvane: http://www.tolvane.com.au/#home4 - This page is a good one as far as selling services and information on the company. I quite like it.

MirefoldIT: http://www.mirefoldit.com.au/ - While I don’t think is particularly creative, it does practically depict the services we offer in a fairly clear way and might be a bit of a basic (albeit dull) template to follow.

JDP: https://store.jdp.com/us/Product-Family/JDP-Advisory-Services/JDP-Cloud-Advisory-Service/p/JDP-Services-Cloud-Advisory - This offers substantial information but is probably a little confusing although the roll-over drop down menus have merit.

ZEV: http://www.zev.net.au/en/services/ - While this in not quite what we are looking for, the colour scheme gives it more gravitas and quality.

As another reference, this website and the way they present their case studies is also something we like, although I’d like them shown 3 up, side by side…. https://www.qandelby.com/case-studies.

We have added a page layout and page purpose document.

Target Market(s)

Corporates, small - medium business, direct referrals, via search results

Industry/Entity Type

Business

Number of Pages Required

1 page

Font styles to use
Sans Serif

Colors
85abd2
0455a3
000000
f37122
5c5c5c

Requirements
Must have
• Website must be mobile device compatible.
• Concept design for the home page.
Nice to have
• We would love to see a design feature based on our name, logo, or industry, which can run through banners and other collateral (twitter banner, ads on Google, corporate documents etc).

```html
<!DOCTYPE html>
<html lang="en">
<head>
<meta charset="utf-8">
<title>Brellomint — Impartial Cloud Solutions</title>
<link href="https://fonts.googleapis.com/css2?family=Open+Sans:wght@400;600;700&family=Dancing+Script:wght@400&display=swap" rel="stylesheet">
<style>
:root{
  --orange:#f05a28;
  --orange-soft:#f37122;
  --black:#000;
  --ink:#222;
  --grey:#5c5c5c;
  --dark:#121316;
  --white:#fff;
  --line:#d8d8d8;
}
*{box-sizing:border-box;margin:0;padding:0}
html,body{width:1200px;height:2778px;overflow:hidden}
body{position:relative;background:var(--white);font-family:Arial,Helvetica,sans-serif;color:var(--ink)}
.abs{position:absolute}
.center{left:0;width:1200px;text-align:center}
.heading{font-family:"Open Sans",Arial,sans-serif}

/* header */
.site-header{top:0;left:0;width:1200px;height:113px;background:var(--white)}
.brand{left:93px;top:30px;display:flex;align-items:center;gap:14px}
.brand-mark{width:40px;height:40px;background:var(--orange)}
.brand-name{font-family:"Open Sans",Arial,sans-serif;font-weight:600;font-size:38px;letter-spacing:1px;color:var(--ink)}
.search{left:874px;top:31px;width:232px;height:39px;border:1px solid var(--line);border-radius:3px;font-size:12px;color:#999;padding:11px 14px}
.search svg{position:absolute;right:12px;top:8px}

.main-nav{left:93px;top:113px;width:1014px;height:50px;background:var(--orange);display:flex;align-items:center;justify-content:space-between;padding:0 12px;z-index:2}
.main-nav a{color:var(--white);text-decoration:none;font-size:14px}

/* hero */
.hero{top:113px;left:0;width:1200px;height:570px;background:linear-gradient(160deg,#3a3a3a 0%,#9a9a9a 35%,#e4e4e4 50%,#8a8a8a 65%,#2e2e2e 100%)}
.hero-title{top:380px;font-size:36px;font-weight:700;color:var(--orange);letter-spacing:.5px}
.hero-box{left:335px;top:437px;width:530px;height:65px;background:rgba(70,70,70,.85);color:var(--white);font-size:13px;line-height:22px;text-align:center;padding:10px 20px}

/* intro band */
.intro{top:683px;left:0;width:1200px;height:226px;background:var(--orange-soft)}
.intro-title{top:34px;font-size:36px;font-weight:600;color:var(--white)}
.intro-rule{top:82px;left:520px;width:160px;height:2px;background:var(--white)}
.intro-text{top:96px;left:170px;width:860px;font-size:13px;line-height:22px;color:var(--white);text-align:center}
.cta{left:491px;top:158px;width:205px;height:43px;background:var(--black);color:var(--white);font-size:13px;display:flex;align-items:center}
.cta span{flex:1;text-align:center}
.cta i{width:36px;height:43px;border-left:1px solid #444;display:flex;align-items:center;justify-content:center}

/* services */
.service{width:204px;text-align:center}
.service-label{position:absolute;top:126px;left:0;width:204px;font-family:"Open Sans",Arial,sans-serif;font-weight:600;font-size:15px;line-height:22px;color:var(--orange)}

/* testimonial */
.testimonial{top:1357px;left:0;width:1200px;height:312px;background:linear-gradient(180deg,#2a2c30 0%,#0d0e10 100%)}
.t-title{top:26px;font-size:22px;font-weight:600;color:var(--white)}
.t-rule{top:60px;left:555px;width:90px;height:2px;background:var(--orange)}
.t-quote{top:166px;left:148px;width:908px;font-size:13px;line-height:23px;color:var(--white);text-align:center}
.t-by{top:245px;font-size:14px;color:var(--orange)}
.t-company{top:266px;font-size:14px;color:var(--white)}

/* what we do */
.ww-title{top:1736px;font-size:17px;font-weight:600;color:var(--grey);letter-spacing:.5px}
.ww-rule{top:1764px;left:555px;width:90px;height:2px;background:var(--orange)}
.ww-text{top:1788px;left:160px;width:880px;font-size:13px;line-height:23px;color:var(--grey);text-align:center}
.ww-visual{left:102px;top:1880px;width:435px;height:352px;background:linear-gradient(135deg,#1d2430 0%,#3d4652 55%,#c9ccd0 100%)}
.video-cue{left:689px;top:1862px;font-family:"Dancing Script",cursive;font-size:32px;color:var(--ink)}
.video-frame{left:691px;top:1920px;width:413px;height:269px;background:linear-gradient(135deg,#b7b3ad 0%,#dcdad6 50%,#8c8a86 100%)}

/* contact */
.contact{top:2311px;left:0;width:1200px;height:421px;background:linear-gradient(180deg,#0d0e12 0%,#1e2228 100%)}
.c-title{top:28px;font-size:17px;font-weight:600;color:var(--white)}
.c-rule{top:56px;left:555px;width:90px;height:2px;background:var(--orange)}
.c-item{left:92px;display:flex;align-items:center;gap:20px;color:var(--white);font-family:"Open Sans",Arial,sans-serif;font-size:17px;line-height:24px}
.field{left:565px;width:541px;border:1px solid #555;background:rgba(0,0,0,.25);color:#888;font-size:12px;padding:12px 10px}
.submit{left:565px;top:337px;width:109px;height:34px;background:var(--orange);color:var(--white);font-family:"Open Sans",Arial,sans-serif;font-size:16px;font-weight:600;text-align:center;line-height:34px}

.site-footer{top:2732px;left:0;width:1200px;height:46px;background:var(--orange);color:var(--white);font-size:12px;text-align:center;line-height:46px}
</style>
</head>
<body>

<header class="site-header abs">
  <div class="brand abs"><span class="brand-mark"></span><span class="brand-name">BRELLOMINT</span></div>
  <div class="search abs">Search...
    <svg width="22" height="22" viewBox="0 0 22 22"><circle cx="9" cy="9" r="7" fill="none" stroke="#999" stroke-width="2.5"/><line x1="14" y1="14" x2="20" y2="20" stroke="#999" stroke-width="3"/></svg>
  </div>
</header>

<nav class="main-nav abs">
  <a>Home</a><a>About Us</a><a>Industry Specialties</a><a>Solutions</a><a>The Company We Keep</a><a>Case Studies and Testimonials</a><a>FAQ's</a><a>Blog</a><a>Contact Us</a>
</nav>

<section class="hero abs" role="img" aria-label="Black and white photo looking up between city skyscrapers">
  <h1 class="hero-title heading abs center" style="top:267px">IMPARTIAL CLOUD SOLUTIONS</h1>
  <p class="hero-box abs" style="top:324px">Sed ut perspiciatis unde omnis iste natus error sit voluptatem accusantium doloremque laudantium, totam rem aperiam,</p>
</section>

<section class="intro abs">
  <h2 class="intro-title heading abs center">IMPARTIAL CLOUD SOLUTIONS</h2>
  <div class="intro-rule abs"></div>
  <p class="intro-text abs">Sed ut perspiciatis unde omnis iste natus error sit voluptatem accusantium doloremque laudantium, totam rem aperiam, eaque ipsa quae ab illo inventore veritatis et quasi architecto beatae vitae dicta sunt explicabo.</p>
  <div class="cta abs"><span>Book A free Consultaion</span><i><svg width="14" height="10" viewBox="0 0 14 10"><path d="M0 5h11M7 1l4 4-4 4" fill="none" stroke="#fff" stroke-width="2"/></svg></i></div>
</section>

<section class="services">
  <svg class="abs" style="left:0;top:1000px" width="1200" height="240" viewBox="0 0 1200 240">
    <defs>
      <g id="tile">
        <polygon points="0,-102 102,0 0,102 -102,0" fill="#fff" stroke="#f05a28" stroke-width="2"/>
        <polygon points="0,-83 83,0 0,83 -83,0" fill="#000"/>
      </g>
    </defs>
    <g transform="translate(194,117)"><use href="#tile"/><path d="M0-20C-8-6-13 2-13 8a13 13 0 0 0 26 0C13 2 8-6 0-20z" fill="#f05a28"/></g>
    <g transform="translate(398,117)"><use href="#tile"/><rect x="-15" y="-22" width="30" height="44" rx="3" fill="none" stroke="#f05a28" stroke-width="3"/><rect x="-10" y="-16" width="20" height="8" fill="#f05a28"/><g fill="#f05a28"><rect x="-10" y="-3" width="5" height="5"/><rect x="-2.5" y="-3" width="5" height="5"/><rect x="5" y="-3" width="5" height="5"/><rect x="-10" y="5" width="5" height="5"/><rect x="-2.5" y="5" width="5" height="5"/><rect x="5" y="5" width="5" height="5"/><rect x="-10" y="13" width="5" height="5"/><rect x="-2.5" y="13" width="5" height="5"/><rect x="5" y="13" width="5" height="5"/></g></g>
    <g transform="translate(602,117)"><use href="#tile"/><rect x="-24" y="-18" width="48" height="30" rx="2" fill="none" stroke="#f05a28" stroke-width="3"/><path d="M-6 12v8h12v-8M-12 21h24" stroke="#f05a28" stroke-width="3" fill="none"/></g>
    <g transform="translate(806,117)"><use href="#tile"/><path d="M0-18a14 14 0 0 0-8 25v7h16v-7a14 14 0 0 0-8-25z" fill="none" stroke="#f05a28" stroke-width="2.5"/><path d="M-6 19h12M-4 24h8" stroke="#f05a28" stroke-width="2.5"/><text x="0" y="6" text-anchor="middle" font-family="Arial,sans-serif" font-size="16" font-weight="700" fill="#f05a28">$</text><g stroke="#f05a28" stroke-width="2"><path d="M0-24v-6M-18-16l-5-4M18-16l5-4M-22 0h-6M22 0h6"/></g></g>
    <g transform="translate(1009,117)"><use href="#tile"/><g fill="#f05a28"><circle cx="0" cy="-10" r="7"/><path d="M-12 14a12 12 0 0 1 24 0z"/><circle cx="-17" cy="-5" r="5"/><path d="M-28 14a11 10 0 0 1 14-10v10z"/><circle cx="17" cy="-5" r="5"/><path d="M28 14a11 10 0 0 0-14-10v10z"/></g></g>
  </svg>
  <div class="service abs" style="left:92px;top:1120px"><p class="service-label">System Selection</p></div>
  <div class="service abs" style="left:296px;top:1120px"><p class="service-label">Accounting Systems<br>&amp; Conversions</p></div>
  <div class="service abs" style="left:500px;top:1120px"><p class="service-label">Integration</p></div>
  <div class="service abs" style="left:704px;top:1120px"><p class="service-label">Business Inventory</p></div>
  <div class="service abs" style="left:907px;top:1120px"><p class="service-label">Business Project &amp;<br>Job Management</p></div>
</section>

<section class="testimonial abs" role="img" aria-label="Dark photo of an empty boardroom table and chairs">
  <h2 class="t-title heading abs center">Testimonial</h2>
  <div class="t-rule abs"></div>
  <svg class="abs" style="left:568px;top:80px" width="64" height="64" viewBox="0 0 64 64"><circle cx="32" cy="32" r="32" fill="#f05a28"/><path d="M16 20h22v14H26l-6 5v-5h-4z" fill="none" stroke="#fff" stroke-width="2.5" stroke-linejoin="round"/><path d="M40 26h8v14h-4v5l-6-5H28v-3" fill="none" stroke="#fff" stroke-width="2.5" stroke-linejoin="round"/></svg>
  <p class="t-quote abs" style="top:159px">Lorem ipsum dolor sit amet, consectetur adipiscing elit, sed do eiusmod tempor incididunt ut labore et dolore magna aliqua. Ut enim ad minim velit esse cillum dolore eu fugiat nulla pariatur. Excepteur sint occaecat cupidatat non proident, sunt in culpa qui officia deserunt mollit anim id est laborum Sed ut perspiciatis unde omnis iste natus error sit voluptatem doloremque.</p>
  <p class="t-by abs center">By John Doe</p>
  <p class="t-company abs center">Company Name</p>
</section>

<section class="what-we-do">
  <h2 class="ww-title heading abs center">WHAT WE DO</h2>
  <div class="ww-rule abs"></div>
  <p class="ww-text abs">Lorem ipsum dolor sit amet, consectetur adipiscing elit, sed do eiusmod tempor incididunt ut labore et dolore magna aliqua. Ut enim ad minim veniam, quis nostrud exercitation ullamco laboris nisi ut aliquip ex ea commodo consequat.</p>
  <div class="ww-visual abs" role="img" aria-label="Desktop monitors showing a business growth graphic"></div>
  <p class="video-cue abs">Click For Play Video</p>
  <div class="video-frame abs" role="img" aria-label="Video still of a man working at a laptop in a bright office">
    <svg class="abs" style="left:182px;top:92px" width="76" height="76" viewBox="0 0 76 76"><circle cx="38" cy="38" r="36" fill="rgba(0,0,0,.15)" stroke="#fff" stroke-width="3"/><path d="M30 24l22 14-22 14z" fill="#f05a28"/></svg>
  </div>
</section>

<section class="contact abs">
  <h2 class="c-title heading abs center">GET IN TUCH</h2>
  <div class="c-rule abs"></div>

  <div class="c-item abs" style="top:103px">
    <svg width="68" height="68" viewBox="0 0 68 68"><polygon points="34,0 68,34 34,68 0,34" fill="#fff"/><path d="M26 22c2-2 4-2 5 0l3 5c1 2 0 3-1 4l-2 2c1 3 4 6 7 7l2-2c1-1 2-2 4-1l5 3c2 1 2 3 0 5-3 3-7 4-12 1-6-4-10-8-13-14-2-4-1-7 2-10z" fill="#f05a28"/></svg>
    <span>555.210.4418</span>
  </div>
  <div class="c-item abs" style="top:196px">
    <svg width="68" height="68" viewBox="0 0 68 68"><polygon points="34,0 68,34 34,68 0,34" fill="#fff"/><rect x="20" y="25" width="28" height="19" fill="#f05a28"/><path d="M20 25l14 11 14-11" fill="none" stroke="#fff" stroke-width="2"/></svg>
    <span>info@brellomint.com.au</span>
  </div>
  <div class="c-item abs" style="top:288px">
    <svg width="68" height="68" viewBox="0 0 68 68"><polygon points="34,0 68,34 34,68 0,34" fill="#fff"/><path d="M34 16a11 11 0 0 0-11 11c0 9 11 22 11 22s11-13 11-22a11 11 0 0 0-11-11z" fill="#f05a28"/><circle cx="34" cy="27" r="4.5" fill="#fff"/></svg>
    <span>Melbourne, Victoria<br>1300 555 017</span>
  </div>

  <div class="field abs" style="top:113px;height:43px">Full Name</div>
  <div class="field abs" style="top:178px;height:43px">Email Address</div>
  <div class="field abs" style="top:243px;height:72px">Message</div>
  <div class="submit abs">SUBMIT</div>
</section>

<footer class="site-footer abs">Copyright © 2014. All Rights Reserved</footer>

</body>
</html>
```